Mission statement design for a secondary school

We have the content of our mission statement and need an appealing layout. The design should fit on a poster or A4 page. The content grouping in the document should also be graphically recognizable. Our target group are young people and their parents as well as the school staff, which is why we need a modern design that is not out after 2 years. It must be easy to grasp visually and graphically simple.

Target Market(s)

Actors of the school

Requirements
Must have
• cantonal logo including school name see document can be integrated as a header
Should not have
• References to trademarks or third parties

```html
<!DOCTYPE html>
<html lang="de">
<head>
<meta charset="utf-8">
<title>Unser Leitbild</title>
<link rel="stylesheet" href="https://fonts.googleapis.com/css2?family=Barlow:wght@700&family=Barlow+Semi+Condensed:wght@700&family=Barlow+Condensed:wght@400;500&family=Nunito:wght@500&display=swap">
<style>
  :root {
    --paper: #f7f3f2;
    --title: #0f72a6;
    --band-haltung: #49b8d6;
    --band-lernen: #1a94c4;
    --band-entwicklung: #1a7289;
    --band-gemeinschaft: #134a5f;
    --text-light: #ffffff;
    --footer-text: #134a5f;
  }
  * { margin: 0; padding: 0; box-sizing: border-box; }
  html, body { width: 900px; height: 1200px; overflow: hidden; background: var(--paper); }
  .poster { position: relative; width: 900px; height: 1200px; background: var(--paper); }
  .poster-title {
    position: absolute; top: 56px; left: 0; width: 900px; text-align: center;
    font-family: "Barlow", sans-serif; font-weight: 700; font-size: 102px;
    line-height: 1; color: var(--title); letter-spacing: 0;
  }
  .section { position: absolute; left: 0; width: 900px; color: var(--text-light); }
  .section--haltung { top: 198px; height: 175px; background: var(--band-haltung); }
  .section--lernen { top: 373px; height: 263px; background: var(--band-lernen); }
  .section--entwicklung { top: 636px; height: 246px; background: var(--band-entwicklung); }
  .section--gemeinschaft { top: 882px; height: 178px; background: var(--band-gemeinschaft); }
  .section-icon {
    position: absolute; left: 38px; width: 130px; height: 130px;
    border-radius: 14px; background: rgba(255,255,255,0.16);
  }
  .section--haltung .section-icon { top: 22px; }
  .section--lernen .section-icon { top: 42px; }
  .section--entwicklung .section-icon { top: 38px; }
  .section--gemeinschaft .section-icon { top: 22px; }
  .section-content { position: absolute; left: 187px; top: 14px; right: 14px; }
  .section-heading {
    font-family: "Barlow Semi Condensed", sans-serif; font-weight: 700;
    font-size: 48px; line-height: 46px; letter-spacing: 0.5px;
  }
  .section-list { list-style: none; margin-top: 1px; }
  .section-list li {
    font-family: "Barlow Condensed", sans-serif; font-weight: 400;
    font-size: 22.5px; line-height: 23.6px;
  }
  .section--haltung .section-list li {
    font-family: "Nunito", sans-serif; font-weight: 500; font-size: 18px;
  }
  .brand {
    position: absolute; right: 32px; top: 1118px;
    font-family: "Barlow Condensed", sans-serif; font-weight: 500; font-size: 30px;
    line-height: 30px; color: var(--footer-text);
  }
</style>
</head>
<body>
<main class="poster">
  <h1 class="poster-title">UNSER LEITBILD</h1>

  <section class="section section--haltung">
    <div class="section-icon" role="img" aria-label="Icon: Kopf mit Häkchen"></div>
    <div class="section-content">
      <h2 class="section-heading">HALTUNG</h2>
      <ul class="section-list">
        <li>stehen die Lernenden im Mittelpunkt.</li>
        <li>ist Integration selbstverständlich.</li>
        <li>begegnen wir uns respektvoll und wertschätzend.</li>
        <li>setzen wir uns für lebenslanges Lernen ein.</li>
      </ul>
    </div>
  </section>

  <section class="section section--lernen">
    <div class="section-icon" role="img" aria-label="Icon: lesende Person mit Buch"></div>
    <div class="section-content">
      <h2 class="section-heading">LERNEN</h2>
      <ul class="section-list">
        <li>Wir begleiten unsere Lernenden hin zur Selbständigkeit.</li>
        <li>Wir unterstützen unsere Lernenden in ihrem individuellen Kompetenzerwerb.</li>
        <li>Wir ermöglichen allen Lernenden Erfolge.</li>
        <li>Die Unterrichtsinhalte orientieren sich an aktuellen Themen.</li>
        <li>Wir beurteilen transparent.</li>
        <li>Wir begegnen Heterogenität mit multiprofessionellen Teams.</li>
        <li>Wir schaffen eine wertschätzende und förderliche Atmosphäre.</li>
        <li>Unsere Schule bietet eine zeitgemässe Infrastruktur.</li>
      </ul>
    </div>
  </section>

  <section class="section section--entwicklung">
    <div class="section-icon" role="img" aria-label="Icon: Person mit aufsteigendem Pfeil"></div>
    <div class="section-content">
      <h2 class="section-heading">ENTWICKLUNG</h2>
      <ul class="section-list">
        <li>Wir entwickeln unsere Schule gemeinsam.</li>
        <li>Wir setzen unsere Fähigkeiten und Kräfte gezielt ein.</li>
        <li>Alle tragen Verantwortung.</li>
        <li>Wir lernen alle voneinander.</li>
        <li>Wir bilden uns kontinuierlich weiter.</li>
        <li>Wir reflektieren unser Handeln.</li>
        <li>Wir sind innovativ und gehen mutig unseren Weg.</li>
      </ul>
    </div>
  </section>

  <section class="section section--gemeinschaft">
    <div class="section-icon" role="img" aria-label="Icon: vier ineinandergreifende Hände"></div>
    <div class="section-content">
      <h2 class="section-heading">GEMEINSCHAFT</h2>
      <ul class="section-list">
        <li>Wir legen Wert auf eine offene Kommunikation.</li>
        <li>Unsere pädagogische Zusammenarbeit basiert auf einer professionellen Haltung.</li>
        <li>Die Eltern sind ein Teil unserer Schulgemeinschaft und tragen Verantwortung.</li>
        <li>Wir haben an unserer Schule Freiräume innerhalb klarer Rahmenbedingungen.</li>
      </ul>
    </div>
  </section>

  <footer class="brand">Talheim Land</footer>
</main>
</body>
</html>
```